Process Diagram - Circular Economy

I would like for a designer to take this rough sketch and turn it into a high quality design which can be used in a business presentation. Seeking to get both PDF and Jpeg file versions of the finished product.

Colours don't have to be the exact same as the rough sketch PDF, the green used is pretty ugly so open to some changes.

Target Market(s)

Corporate audience

Requirements
Must have
• Clear text for each party; VENOR, TORVIN, BUYER

Smaller text for the functions; marketing, recovery, logistics, cleaning, decontamination, testing & re-certification, storage, engineering suitability

```html
<!DOCTYPE html>
<html lang="en">
<head>
<meta charset="utf-8">
<title>Process Diagram – Circular Economy</title>
<link rel="stylesheet" href="https://fonts.googleapis.com/css2?family=Oswald:wght@500;700&family=Montserrat:wght@600;700&family=Great+Vibes&display=swap">
<style>
  :root {
    --backdrop: #b9b7c8;
    --navy-purple: #2a0f5e;
    --vendor-purple: #4e1f8c;
    --vendor-purple-dark: #3a1677;
    --buyer-red: #f0394f;
    --accent-blue: #1f8fe5;
    --accent-red: #ee3a55;
    --wheel-light: #d8eefa;
    --wheel-dark: #15589f;
    --wheel-mid: #2a86d2;
    --wheel-bright: #3ea6ea;
    --brand-blue: #1c3f8f;
    --script-purple: #3d1a6e;
    --script-red: #a3122c;
    --white: #ffffff;
  }
  html, body {
    margin: 0;
    padding: 0;
    width: 1200px;
    height: 1200px;
    overflow: hidden;
    background: var(--backdrop);
  }
  .canvas {
    display: block;
    width: 1200px;
    height: 1200px;
  }
  .title { font-family: "Oswald", sans-serif; font-weight: 700; fill: var(--white); }
  .party-label { font-family: "Oswald", sans-serif; font-weight: 700; fill: var(--white); }
  .life-script { font-family: "Great Vibes", cursive; }
  .life-script--end { fill: var(--script-purple); }
  .life-script--new { fill: var(--script-red); }
  .function-label { font-family: "Montserrat", sans-serif; font-weight: 700; fill: var(--white); font-size: 6.5px; text-anchor: middle; }
  .brand-name { font-family: "Oswald", sans-serif; font-weight: 700; fill: var(--brand-blue); letter-spacing: 1px; }
  .web-address { font-family: "Montserrat", sans-serif; font-weight: 700; fill: var(--white); }
  .icon { fill: none; stroke: var(--white); stroke-width: 1.4; stroke-linecap: round; stroke-linejoin: round; }
</style>
</head>
<body>
<svg class="canvas" viewBox="0 0 1000 1000" xmlns="http://www.w3.org/2000/svg">
  <defs>
    <linearGradient id="vendorBand" x1="0" y1="0" x2="1" y2="0">
      <stop offset="0" stop-color="var(--vendor-purple)"/>
      <stop offset="1" stop-color="var(--vendor-purple-dark)"/>
    </linearGradient>
    <linearGradient id="wheelRing" x1="0" y1="0" x2="1" y2="1">
      <stop offset="0" stop-color="var(--accent-red)"/>
      <stop offset="0.55" stop-color="#6a1f8e"/>
      <stop offset="1" stop-color="var(--navy-purple)"/>
    </linearGradient>
    <linearGradient id="brandRule" x1="0" y1="0" x2="1" y2="0">
      <stop offset="0" stop-color="var(--vendor-purple)"/>
      <stop offset="1" stop-color="var(--accent-red)"/>
    </linearGradient>
  </defs>

  <g class="slide">
    <rect class="slide-body" x="30" y="170" width="940" height="665" fill="var(--white)"/>

    <g class="header">
      <rect x="30" y="170" width="940" height="88" fill="var(--navy-purple)"/>
      <rect x="30" y="212" width="225" height="5" fill="var(--accent-blue)"/>
      <rect x="682" y="212" width="288" height="5" fill="var(--accent-red)"/>
      <text class="title" x="470" y="237" font-size="50" text-anchor="middle">PROCESS DIAGRAM</text>
    </g>

    <g class="buyer-arrow">
      <polygon points="505,432 785,343 777,315 860,352 818,440 810,412 550,497" fill="var(--buyer-red)"/>
      <text class="party-label" font-size="36" transform="translate(628,462) rotate(-17)">BUYER</text>
      <circle cx="762" cy="392" r="36" fill="#f4707f" role="img" aria-label="Buyer with shopping cart and price tag"/>
      <text class="life-script life-script--new" font-size="30" transform="translate(592,382) rotate(-15)">New Life</text>
    </g>

    <g class="vendor-band">
      <path d="M210.6,325 L555.6,445 L524.4,535 L179.4,415 A47.5,47.5 0 0 1 210.6,325 Z" fill="url(#vendorBand)"/>
      <circle cx="218" cy="378" r="38" fill="#7447b0" role="img" aria-label="Vendors at a desk with money and gear"/>
      <text class="party-label" font-size="36" transform="translate(278,412) rotate(19)">VENDOR</text>
      <text class="life-script life-script--end" font-size="30" transform="translate(300,348) rotate(15)">End of Life</text>
    </g>

    <g class="process-wheel">
      <circle cx="480" cy="622" r="172" fill="url(#wheelRing)"/>
      <circle cx="480" cy="622" r="160" fill="var(--wheel-light)"/>
      <g class="wheel-segments" stroke="var(--wheel-light)" stroke-width="4">
        <path d="M420.7,478.8 A155,155 0 0 1 539.3,478.8 L507.6,555.5 A72,72 0 0 0 452.4,555.5 Z" fill="var(--wheel-bright)"/>
        <path d="M539.3,478.8 A155,155 0 0 1 623.2,562.7 L546.5,594.4 A72,72 0 0 0 507.6,555.5 Z" fill="var(--wheel-dark)"/>
        <path d="M623.2,562.7 A155,155 0 0 1 623.2,681.3 L546.5,649.6 A72,72 0 0 0 546.5,594.4 Z" fill="var(--wheel-mid)"/>
        <path d="M623.2,681.3 A155,155 0 0 1 539.3,765.2 L507.6,688.5 A72,72 0 0 0 546.5,649.6 Z" fill="var(--wheel-dark)"/>
        <path d="M539.3,765.2 A155,155 0 0 1 420.7,765.2 L452.4,688.5 A72,72 0 0 0 507.6,688.5 Z" fill="var(--wheel-bright)"/>
        <path d="M420.7,765.2 A155,155 0 0 1 336.8,681.3 L413.5,649.6 A72,72 0 0 0 452.4,688.5 Z" fill="var(--wheel-dark)"/>
        <path d="M336.8,681.3 A155,155 0 0 1 336.8,562.7 L413.5,594.4 A72,72 0 0 0 413.5,649.6 Z" fill="var(--wheel-mid)"/>
        <path d="M336.8,562.7 A155,155 0 0 1 420.7,478.8 L452.4,555.5 A72,72 0 0 0 413.5,594.4 Z" fill="var(--wheel-dark)"/>
      </g>

      <g class="step step--engineering">
        <g transform="translate(480,491)">
          <circle class="icon" r="6"/>
          <circle class="icon" r="2.2"/>
        </g>
        <text class="function-label" x="480" y="509">ENGINEERING</text>
        <text class="function-label" x="480" y="517">SUSTAINABILITY</text>
      </g>

      <g class="step step--storage">
        <path class="icon" transform="translate(561,531)" d="M-9,7 V-3 L0,-8 L9,-3 V7 Z M-4,7 V2 H4 V7"/>
        <text class="function-label" x="561" y="550">STORAGE</text>
      </g>

      <g class="step step--testing">
        <g transform="translate(594,605)">
          <rect class="icon" x="-6" y="-8" width="12" height="16" rx="1"/>
          <path class="icon" d="M-3,-3 H3 M-3,1 H3 M-3,4.5 H1"/>
        </g>
        <text class="function-label" x="594" y="625">TESTING &amp;</text>
        <text class="function-label" x="594" y="633">RE-CERTIFICATION</text>
      </g>

      <g class="step step--decontamination">
        <g transform="translate(561,692)">
          <path class="icon" d="M-2,-8 C-5,-2 -8,1 -8,4 A6,6 0 0 0 4,4 C4,1 1,-2 -2,-8 Z"/>
          <circle class="icon" cx="7" cy="-6" r="3"/>
        </g>
        <text class="function-label" x="561" y="712">DECONTAMINATION</text>
      </g>

      <g class="step step--cleaning">
        <g transform="translate(480,724)">
          <path class="icon" d="M-3,-8 L-1,-2 L5,0 L-1,2 L-3,8 L-5,2 L-11,0 L-5,-2 Z"/>
          <path class="icon" d="M7,-9 L8,-6.5 L10.5,-5.5 L8,-4.5 L7,-2 L6,-4.5 L3.5,-5.5 L6,-6.5 Z"/>
        </g>
        <text class="function-label" x="480" y="744">CLEANING</text>
      </g>

      <g class="step step--logistics">
        <g transform="translate(399,691)">
          <rect class="icon" x="-8" y="-6" width="7" height="6"/>
          <rect class="icon" x="1" y="-6" width="7" height="6"/>
          <rect class="icon" x="-3.5" y="-12" width="7" height="6"/>
          <path class="icon" d="M-6,3 V9 M-8,7 L-6,9 L-4,7 M0,3 V9 M-2,7 L0,9 L2,7 M6,3 V9 M4,7 L6,9 L8,7"/>
        </g>
        <text class="function-label" x="399" y="712">LOGISTICS</text>
      </g>

      <g class="step step--recovery">
        <g transform="translate(365,607)">
          <path class="icon" d="M7,0 A7,7 0 1 0 0,7" stroke-dasharray="2.5 2"/>
          <path class="icon" d="M-2,4 L0,7 L-3,9"/>
        </g>
        <text class="function-label" x="365" y="630">RECOVERY</text>
      </g>

      <g class="step step--marketing">
        <g transform="translate(399,530)">
          <path class="icon" d="M-9,-3 H-5 L4,-8 V8 L-5,3 H-9 Z M-6,3 L-4,9"/>
          <path class="icon" d="M7,-4 L10,-5.5 M7.5,0 H11 M7,4 L10,5.5"/>
        </g>
        <text class="function-label" x="399" y="550">MARKETING</text>
      </g>

      <g class="wheel-hub">
        <text class="brand-name" x="486" y="630" font-size="26" text-anchor="middle">TORVIN</text>
        <rect x="444" y="637" width="84" height="3" fill="url(#brandRule)"/>
      </g>
    </g>

    <g class="footer">
      <path d="M738,790 H970 V822 H722 V806 A16,16 0 0 1 738,790 Z" fill="var(--accent-blue)"/>
      <text class="web-address" x="846" y="812" font-size="15" text-anchor="middle">WWW.TORVINLOOP.COM</text>
      <rect x="30" y="822" width="940" height="13" fill="var(--navy-purple)"/>
    </g>
  </g>
</svg>
</body>
</html>
```